BrindleStaffing Business Card Design

We are a staffing company finding positions for dedicated nurses and physicians.

Target Market(s)

Business Professionals

Industry/Entity Type

Staffing

Contact Information for Business Card

Gregory Malden
Chairman
417 39th Crescent South
SAINT PETERSBURG FL 33719
813-555-0147 Mobile
813-555-0183 Fax
gmalden@brindlestaffing.example
www.brindlestaffing.example

Font styles to use
Sans Serif

Colors
fbee3e
f04a50
f37122

Requirements
Must have
• Logo Attached, see colors below. We'd like to see Yellow, Orange and Red.

```html
<!DOCTYPE html>
<html lang="en">
<head>
<meta charset="utf-8">
<title>BrindleStaffing Business Card</title>
<link rel="stylesheet" href="https://fonts.googleapis.com/css2?family=Figtree:wght@400;500;700;800&display=swap">
<style>
  :root {
    --page: #ffffff;
    --orange: #f37122;
    --yellow: #f5ee3e;
    --red: #f04a50;
    --ink: #1f1d1a;
    --white: #ffffff;
  }
  * { margin: 0; padding: 0; box-sizing: border-box; }
  html, body {
    width: 1200px; height: 1200px; overflow: hidden;
    background: var(--page);
    font-family: "Figtree", sans-serif;
  }
  .canvas { position: relative; width: 1200px; height: 1200px; }
  .card {
    position: absolute; left: 240px; width: 720px; height: 420px; overflow: hidden;
  }
  .card-front { top: 142px; background: var(--orange); }
  .card-back { top: 638px; background: var(--yellow); }

  .front-wordmark {
    position: absolute; left: 0; right: 0; top: 174px;
    text-align: center; color: var(--white);
    font-weight: 700; font-size: 60px; letter-spacing: -1px; line-height: 1;
  }

  .holder { position: absolute; left: 38px; top: 144px; }
  .holder-name {
    color: var(--red); font-weight: 700; font-size: 32px; line-height: 1; letter-spacing: 0.2px;
  }
  .holder-title {
    margin-top: 10px; color: var(--ink); font-weight: 500; font-size: 17px;
  }
  .address {
    position: absolute; left: 38px; top: 235px;
    color: var(--ink); font-weight: 500; font-size: 17px; line-height: 24px;
  }
  .contact-list {
    position: absolute; left: 38px; top: 295px; list-style: none;
    color: var(--ink); font-weight: 500; font-size: 17px; line-height: 25px;
  }
  .contact-list li { display: flex; align-items: center; gap: 11px; }
  .contact-list svg { width: 14px; height: 14px; fill: var(--orange); flex: none; }

  .back-wordmark {
    position: absolute; right: 26px; top: 38px; height: 344px;
    writing-mode: vertical-rl; transform: rotate(180deg);
    color: var(--red); font-weight: 700; font-size: 44px; letter-spacing: -0.5px; line-height: 1;
    text-align: left;
  }
</style>
</head>
<body>
<div class="canvas">
  <section class="card card-front">
    <div class="front-wordmark">BrindleStaffing</div>
  </section>

  <section class="card card-back">
    <div class="holder">
      <div class="holder-name">Gregory Malden</div>
      <div class="holder-title">Founder &amp; CEO</div>
    </div>
    <div class="address">
      <div>417 39th Crescent South</div>
      <div>SAINT PETERSBURG FL 33719</div>
    </div>
    <ul class="contact-list">
      <li>
        <svg viewBox="0 0 16 16" aria-hidden="true"><path d="M3.6 1.2l2.3 2.6-1.3 1.9c.9 2 2.6 3.7 4.6 4.6l1.9-1.3 2.6 2.3-1.2 2.4C7.6 13.4 2.6 8.4 1.2 3.4z"/></svg>
        <span>813-555-0147</span>
      </li>
      <li>
        <svg viewBox="0 0 16 16" aria-hidden="true"><path d="M4 1h8v4H4zM1 6h14v6h-3v3H4v-3H1zm4 4v3h6v-3z"/></svg>
        <span>813-555-0183</span>
      </li>
      <li>
        <svg viewBox="0 0 16 16" aria-hidden="true"><path d="M1 3h14v1.5L8 9 1 4.5zM1 6.3l7 4.5 7-4.5V13H1z"/></svg>
        <span>gmalden@brindlestaffing.example</span>
      </li>
      <li>
        <svg viewBox="0 0 16 16" aria-hidden="true"><path d="M8 1a7 7 0 100 14A7 7 0 008 1zm0 1.5c.8 0 1.8 1.8 2 4.5H6c.2-2.7 1.2-4.5 2-4.5zM2.6 7h2c.1-1.6.5-3 1-3.9A5.6 5.6 0 002.6 7zm8.8 0h2a5.6 5.6 0 00-3-3.9c.5.9.9 2.3 1 3.9zM2.6 9a5.6 5.6 0 003 3.9c-.5-.9-.9-2.3-1-3.9zm3.4 0c.2 2.7 1.2 4.5 2 4.5s1.8-1.8 2-4.5zm5.4 0c-.1 1.6-.5 3-1 3.9a5.6 5.6 0 003-3.9z"/></svg>
        <span>www.brindlestaffing.example</span>
      </li>
    </ul>
    <div class="back-wordmark">BrindleStaffing</div>
  </section>
</div>
</body>
</html>
```